New Corporate website more focused on funnel and great design

Our company, Bold Harbor needs a new website to look like it's from 2021. We work with large businesses in the corporte world and need to reflect that we are professional, focused on our clients, and trsutworthy. It should include some/most of the components from our current site: boldharbor.com but should focus more about getting people to optin to out free downloads, which can be found on this page: https://www.boldharbor.com/get-started-with-a-prep-session/ and this page: https://www.boldharbor.com/team-onboarding/

Our new website should do a better job at explaining what we do, who we serve, and how we fix their problems of onboarding new leaders. Feel free to use dummy text if you are not sure what to put in for certain sections. I also would like to point out that most of the audiance is older, so we don't need anything too younge and flashy, or that is hard it use. it should have big clear fonts, plently of contrast, and work well for poeple who are not good at using the internet. Please use the colors of the logo, and you can add another color or two if you think it's fits

Industry/Entity Type

business consulting

Number of Pages Required

2 page

Font styles to use
Sans Serif

Requirements
Must have
• corporate feel, look professional, focus on getting new leads
Should not have
• cute or children feel

```html
<!DOCTYPE html>
<html lang="en">
<head>
<meta charset="utf-8">
<title>Bold Harbor — Business Performance Consulting</title>
<link href="https://fonts.googleapis.com/css2?family=Montserrat:wght@300;400;500;600;700;800&display=swap" rel="stylesheet">
<style>
:root{
  --blue:#1a8fe3;
  --blue-light:#3aa6f0;
  --navy:#0d4a8f;
  --navy-deep:#0a3b78;
  --ink:#222a36;
  --text:#4a5260;
  --muted:#8a92a0;
  --line:#b9c6e6;
  --ghost:#eef1f6;
  --footer:#1e2b48;
  --white:#ffffff;
  --star:#f5b418;
}
*{box-sizing:border-box;margin:0;padding:0}
html,body{width:1200px;height:4878px;overflow:hidden}
body{position:relative;background:var(--white);font-family:'Montserrat',sans-serif;color:var(--text)}
.abs{position:absolute}
.btn{position:absolute;display:flex;align-items:center;justify-content:center;border-radius:24px;background:var(--blue);color:var(--white);font-weight:700;font-size:12px;letter-spacing:.5px;text-decoration:none}
.photo{position:absolute}

/* hero */
.hero{position:absolute;left:0;top:0;width:1200px;height:712px;background:linear-gradient(180deg,#1c3f72 0%,#2c5a92 40%,#345f8e 70%,#1f3e6a 100%)}
.hero-scene{position:absolute;inset:0;background:radial-gradient(ellipse at 70% 30%,rgba(180,195,215,.45),transparent 55%),radial-gradient(ellipse at 30% 80%,rgba(40,80,140,.6),transparent 60%)}
.brand{position:absolute;display:flex;align-items:center;gap:10px;color:var(--white)}
.brand-mark{width:28px;height:28px;border:2px solid currentColor}
.brand-name{font-size:22px;font-weight:500;line-height:1}
.nav{position:absolute;top:22px;left:0;width:1200px;height:30px}
.nav a{position:absolute;top:0;color:var(--white);font-size:12px;text-decoration:none;font-weight:500}
.nav a.active{font-weight:700}
.nav a.active::after{content:"";position:absolute;left:0;right:0;top:24px;height:2px;background:var(--white)}
.hero-frame{position:absolute;left:278px;top:288px;width:619px;height:170px;border:2px solid var(--white);border-top:none}
.hero-frame::before,.hero-frame::after{content:"";position:absolute;top:0;height:2px;background:var(--white);width:80px}
.hero-frame::before{left:0}.hero-frame::after{right:0}
.hero-title{position:absolute;left:0;width:1200px;text-align:center;color:var(--white)}
.hero-title.light{top:272px;font-size:35px;font-weight:300}
.hero-title.bold{top:318px;font-size:40px;font-weight:700}
.btn.outline{background:transparent;border:2px solid var(--white);gap:8px}

/* section headings */
.ghost{position:absolute;font-weight:800;color:var(--ghost);white-space:nowrap;letter-spacing:3px}
.h2{position:absolute;font-weight:700;color:var(--ink);font-size:30px;line-height:1.2}
.h2 .thin{font-weight:400}
.para{position:absolute;font-size:14px;line-height:28px;color:var(--text)}
.underline{position:absolute;height:3px;width:68px;background:var(--blue)}

/* steps */
.steps-lines{position:absolute;left:0;top:1259px}
.step{position:absolute;width:240px;text-align:center}
.step h3{font-size:13px;font-weight:600;color:var(--ink);line-height:19px}
.step p{font-size:11px;line-height:19px;margin-top:12px}
.hex{position:absolute}

/* services */
.service{position:absolute;width:260px;text-align:center}
.service h3{font-size:14px;font-weight:700;color:var(--ink);line-height:20px}
.service p{font-size:11.5px;line-height:16px;margin-top:8px}
.service-card{position:absolute;left:420px;top:2395px;width:332px;height:337px;background:var(--white);box-shadow:0 6px 26px rgba(20,40,80,.14)}

/* testimonials */
.quote-card{position:absolute;background:var(--white);box-shadow:0 8px 28px rgba(20,40,80,.12)}
.quote-card h4{font-size:17px;font-weight:600;color:var(--ink);line-height:28px}
.quote-card p{font-size:10.5px;line-height:18px;margin-top:12px;color:var(--muted)}
.author{display:flex;align-items:center;gap:12px;margin-top:16px}
.avatar{width:34px;height:34px;border-radius:50%;background:linear-gradient(135deg,#9aa7bd,#5b6a85)}
.author-name{font-size:9px;font-weight:700;color:var(--ink)}
.stars{color:var(--star);font-size:12px;letter-spacing:1px}
.dot{position:absolute;width:11px;height:11px;border-radius:50%;background:#d9dde4}

/* contact */
.contact-band{position:absolute;left:0;top:4104px;width:1200px;height:449px;background:linear-gradient(180deg,#1178d4 0%,#0d5fb6 55%,#0a4d9c 100%)}
.field{position:absolute;background:var(--white);border-radius:2px;display:flex;align-items:center;gap:10px;padding-left:16px;font-size:11px;color:#5a6270}
.field.area{align-items:flex-start;padding-top:14px}

/* footer */
.footer{position:absolute;left:0;top:4553px;width:1200px;height:325px;background:var(--footer);color:var(--white)}
.footer h5{position:absolute;font-size:12px;font-weight:700;letter-spacing:.5px}
.footer .small{position:absolute;font-size:11px;line-height:20px;color:#dfe5ef}
.social{position:absolute;width:24px;height:24px;border-radius:50%;background:var(--white)}
</style>
</head>
<body>

<!-- HERO -->
<header class="hero">
  <div class="hero-scene" role="img" aria-label="Photo of business colleagues reviewing a tablet in a bright office"></div>
  <div class="brand" style="left:104px;top:18px">
    <span class="brand-mark"></span>
    <div class="brand-name">Bold Harbor</div>
  </div>
  <nav class="nav">
    <a class="active" style="left:432px">WHO WE ARE</a>
    <a style="left:577px">WHAT WE DO</a>
    <a style="left:712px">CLIENTS</a>
    <a style="left:814px">BLOG</a>
    <a style="left:899px">RESOURCES</a>
    <a style="left:1024px">CONTACT US</a>
  </nav>
  <div class="hero-frame"></div>
  <h1 class="hero-title light">WE ACCELERATE YOUR</h1>
  <div class="hero-title bold">BUSINESS PERFORMANCE</div>
  <a class="btn" style="left:435px;top:382px;width:154px;height:34px">GET A QUOTE</a>
  <a class="btn outline" style="left:600px;top:382px;width:153px;height:34px">
    <svg width="16" height="16" viewBox="0 0 16 16"><circle cx="8" cy="8" r="8" fill="#fff"/><path d="M6 4.5v7l5.5-3.5z" fill="#1c3f72"/></svg>PLAY VIDEO</a>
</header>

<!-- ABOUT -->
<svg class="photo" style="left:0;top:757px" width="560" height="545" viewBox="0 0 560 545" role="img" aria-label="Photo of a team meeting around a conference table">
  <defs><linearGradient id="gAbout" x1="0" y1="0" x2="1" y2="1"><stop offset="0" stop-color="#c9a25a"/><stop offset=".5" stop-color="#b8c2cf"/><stop offset="1" stop-color="#6d7c92"/></linearGradient></defs>
  <path d="M0 40 C90 -10 210 30 330 60 C470 95 560 170 545 300 C530 440 380 520 220 540 C120 552 40 530 0 500 Z" fill="var(--navy)"/>
  <path d="M0 30 C90 -20 210 18 325 48 C460 82 545 160 532 290 C518 425 375 505 215 525 C120 536 40 515 0 490 Z" fill="url(#gAbout)"/>
</svg>
<div class="ghost" style="left:596px;top:836px;font-size:70px">WHO WE ARE</div>
<h2 class="h2" style="left:602px;top:879px;font-size:32px;font-weight:600">ABOUT BOLD HARBOR</h2>
<p class="para" style="left:606px;top:942px;width:470px">We know, through our personal experiences gained as leaders, that the first 100 days in a critical transition are a crucible of leadership – when managed well, leaders build cohesive teams that succeed. When managed poorlyLorem Ipsum is simply dummy text of the printing and typesetting industry. Lorem Ipsum has been the industry's standard dummy text ever since the 1500s,</p>
<a class="btn" style="left:598px;top:1145px;width:174px;height:49px;font-size:14px">LEARN MORE</a>

<svg class="steps-lines" width="1200" height="150" viewBox="0 0 1200 150">
  <g fill="none" stroke="var(--line)" stroke-width="2">
    <path d="M600 0 V60 Q600 85 575 85 H318 Q293 85 293 110 V135"/>
    <path d="M618 0 V60 Q618 85 643 85 H899 Q924 85 924 110 V135"/>
    <path d="M609 0 V135"/>
  </g>
  <circle cx="293" cy="139" r="6" fill="var(--blue)"/>
  <circle cx="609" cy="139" r="6" fill="var(--navy-deep)"/>
  <circle cx="924" cy="139" r="6" fill="var(--blue)"/>
</svg>

<svg class="hex" style="left:227px;top:1424px" width="132" height="136" viewBox="0 0 132 136">
  <polygon points="66,2 128,36 128,100 66,134 4,100 4,36" fill="#fff" stroke="#dfe6f2" stroke-width="2"/>
  <polygon points="66,14 118,42 118,94 66,122 14,94 14,42" fill="var(--navy)"/>
  <g fill="none" stroke="#fff" stroke-width="2"><rect x="52" y="52" width="28" height="20" rx="2"/><path d="M52 54 L66 64 L80 54"/><circle cx="54" cy="86" r="4"/><circle cx="66" cy="86" r="4"/><circle cx="78" cy="86" r="4"/><path d="M66 72 V80"/></g>
</svg>
<svg class="hex" style="left:543px;top:1424px" width="132" height="136" viewBox="0 0 132 136">
  <polygon points="66,2 128,36 128,100 66,134 4,100 4,36" fill="#fff" stroke="#dfe6f2" stroke-width="2"/>
  <polygon points="66,14 118,42 118,94 66,122 14,94 14,42" fill="var(--navy-deep)"/>
  <g fill="none" stroke="#fff" stroke-width="2"><circle cx="56" cy="56" r="6"/><rect x="66" y="50" width="20" height="12" rx="3"/><rect x="46" y="72" width="20" height="12" rx="3"/><circle cx="78" cy="80" r="6"/><path d="M56 62 V70 M78 62 V72"/></g>
</svg>
<svg class="hex" style="left:858px;top:1424px" width="132" height="136" viewBox="0 0 132 136">
  <polygon points="66,2 128,36 128,100 66,134 4,100 4,36" fill="#fff" stroke="#dfe6f2" stroke-width="2"/>
  <polygon points="66,14 118,42 118,94 66,122 14,94 14,42" fill="var(--blue)"/>
  <g fill="none" stroke="#fff" stroke-width="2"><path d="M46 80 H60 L70 86 H86"/><path d="M58 74 V64 M66 74 V58 M74 74 V62 M82 74 V52"/><path d="M56 58 L70 50 L84 46"/></g>
</svg>

<div class="step" style="left:173px;top:1584px"><h3>GET A HEAD START<br>BEFORE DAY ONE</h3><p>Lorem Ipsum is simply dummy text<br>of the printing and typesetting<br>industry. Lorem Ipsum</p></div>
<div class="step" style="left:489px;top:1584px"><h3>MANAGE THE<br>MESSAGE</h3><p>Lorem Ipsum is simply dummy text of<br>the printing and typesetting industry.<br>Lorem Ipsum</p></div>
<div class="step" style="left:804px;top:1584px"><h3>BUILD THE TEAM &amp;<br>DELIVER RESULTS</h3><p>Lorem Ipsum is simply dummy text of<br>the printing and typesetting industry.<br>Lorem Ipsum</p></div>

<!-- HOW WE HELP -->
<div class="ghost" style="left:60px;top:2170px;font-size:46px;transform:rotate(-90deg);transform-origin:0 0">PERFORMING</div>
<h2 class="h2" style="left:134px;top:1838px">HOW WE HELP<br>YOU SUCCEED</h2>
<p class="para" style="left:132px;top:1918px;width:410px">We know, through our personal experiences gained as leaders, that the first 100 days in a critical transition are a crucible of leadership – when managed well, leaders build cohesive teams that succeed. When managed poorlyLorem Ipsum is simply dummy text of the printing and typesetting industry. Lorem Ipsum</p>
<a class="btn" style="left:134px;top:2114px;width:203px;height:46px;background:var(--navy);font-size:13px">GET A FREE QUOTE</a>
<svg class="photo" style="left:568px;top:1760px" width="580" height="482" viewBox="0 0 580 482" role="img" aria-label="Photo of two business colleagues, a man in a blue shirt and a woman in yellow">
  <defs><linearGradient id="gHelp" x1="0" y1="0" x2="1" y2="1"><stop offset="0" stop-color="#8fb0d6"/><stop offset=".5" stop-color="#5a86b8"/><stop offset="1" stop-color="#d6b44c"/></linearGradient></defs>
  <path d="M60 40 C140 -20 250 20 330 70 C400 110 470 100 540 140 C600 180 580 300 510 390 C440 470 300 500 170 470 C50 440 -10 330 5 220 C15 140 20 80 60 40 Z" fill="url(#gHelp)"/>
</svg>
<svg class="abs" style="left:300px;top:2186px" width="320" height="140" viewBox="0 0 320 140"><path d="M8 0 V30 Q8 58 40 58 H280 Q309 58 309 88 V140" fill="none" stroke="var(--line)" stroke-width="2"/></svg>

<!-- SERVICES -->
<div class="ghost" style="left:0;width:1200px;text-align:center;top:2290px;font-size:70px">WHAT WE DO</div>
<h2 class="h2" style="left:0;width:1200px;text-align:center;top:2310px">SERVICES WE <span class="thin">PROVIDE</span></h2>
<div class="underline" style="left:583px;top:2355px"></div>

<div class="service-card"></div>
<svg class="abs" style="left:198px;top:2420px" width="124" height="104" viewBox="0 0 124 104">
  <path d="M20 10 C50 -8 80 10 105 25 C130 45 124 85 92 98 C60 110 20 100 8 74 C-4 50 -2 24 20 10 Z" fill="var(--navy)"/>
  <g fill="none" stroke="#fff" stroke-width="2"><circle cx="55" cy="40" r="8"/><path d="M40 70 Q40 54 55 54 Q70 54 70 70 Z"/><rect x="66" y="58" width="18" height="14"/></g>
</svg>
<svg class="abs" style="left:530px;top:2416px" width="116" height="112" viewBox="0 0 116 112">
  <path d="M70 4 C100 0 116 30 108 60 C100 92 70 110 40 106 C10 102 -4 78 8 60 C20 44 40 40 48 22 C54 10 60 6 70 4 Z" fill="var(--blue)"/>
  <g fill="none" stroke="#fff" stroke-width="2"><circle cx="58" cy="66" r="10"/><circle cx="58" cy="66" r="3"/><path d="M58 50 V56 M58 76 V82 M42 66 H48 M68 66 H74"/></g>
</svg>
<svg class="abs" style="left:880px;top:2424px" width="124" height="104" viewBox="0 0 124 104">
  <path d="M40 6 C72 -6 110 10 118 42 C124 72 98 100 64 100 C40 100 30 82 16 72 C0 60 2 20 40 6 Z" fill="var(--navy-deep)"/>
  <g fill="none" stroke="#fff" stroke-width="2"><path d="M50 70 L76 44 Q80 36 72 38 L46 64 Z"/><path d="M46 70 L40 76 M52 74 L48 80"/></g>
</svg>

<div class="service" style="left:120px;top:2544px"><h3>EXECUTIVE<br>ONBOARDING</h3><p>For executive leaders taking on new roles, the Bold Harbor 100-Day Action Plan process prepares leaders before the start</p></div>
<div class="service" style="left:456px;top:2547px;width:260px"><h3>TEAM ONBOARDING</h3><p>For leaders integrating teams post acquisition or re-organization, the Bold Harbor 100 Day Action Plan process gets all players</p></div>
<a class="btn" style="left:523px;top:2668px;width:139px;height:38px;font-size:11px">LEARN MORE</a>
<div class="service" style="left:813px;top:2544px"><h3>ACCELERATION<br>&amp; RESTART</h3><p>For executive leaders taking on new roles, the Bold Harbor 100-Day Action Plan process prepares leaders before the start</p></div>

<!-- TESTIMONIALS -->
<div class="ghost" style="left:0;width:1200px;text-align:center;top:2868px;font-size:70px">TESTIMONIALS</div>
<h2 class="h2" style="left:0;width:1200px;text-align:center;top:2888px">WHY OUR CLIENT SAYS</h2>
<div class="underline" style="left:583px;top:2932px"></div>

<svg class="photo" style="left:0;top:2950px" width="475" height="498" viewBox="0 0 475 498" role="img" aria-label="Video thumbnail of a smiling businessman in a suit holding a tablet">
  <defs><linearGradient id="gTesti" x1="0" y1="0" x2="1" y2="1"><stop offset="0" stop-color="#e9edf2"/><stop offset=".5" stop-color="#a9b6c8"/><stop offset="1" stop-color="#2c3f62"/></linearGradient></defs>
  <path d="M0 30 C100 -10 240 20 340 70 C440 120 480 230 460 320 C440 410 360 460 250 470 C150 480 60 498 0 470 Z" fill="var(--navy)"/>
  <path d="M0 18 C100 -22 235 8 332 58 C430 108 466 220 448 308 C428 396 350 446 245 456 C150 465 60 482 0 456 Z" fill="url(#gTesti)"/>
  <circle cx="218" cy="254" r="26" fill="rgba(255,255,255,.75)"/><path d="M210 241 V267 L232 254 Z" fill="#fff"/>
</svg>

<div class="quote-card" style="left:509px;top:3019px;width:438px;height:284px;padding:38px 55px">
  <h4>What ClearPath Guides Experienced After Getting Certified</h4>
  <p>Working with Morgan was easy and exciting. He was able to distill our ideas and keep us focused on what we needed for our website. He was able to speak to us in simple language on the details and operations of our website.</p>
  <div class="author"><span class="avatar"></span><div><div class="author-name">DANIEL REESE</div><div class="stars">★★★★★</div></div></div>
</div>
<div class="quote-card" style="left:986px;top:3022px;width:438px;height:284px;padding:38px 55px;overflow:hidden;opacity:.7">
  <h4>What ClearPath Guides Experienced After Getting Certified</h4>
  <p>Working with Morgan was easy and exciting. He was able to distill our ideas and keep us focused on what we needed for our website. He was able to speak to us in simple language on the details and operations of our website.</p>
  <div class="author"><span class="avatar"></span><div><div class="author-name">DANIEL REESE</div><div class="stars">★★★★★</div></div></div>
</div>
<span class="dot" style="left:728px;top:3340px;background:#9aa3b1"></span>
<span class="dot" style="left:757px;top:3340px"></span>
<span class="dot" style="left:783px;top:3340px"></span>
<svg class="abs" style="left:290px;top:3388px" width="320" height="160" viewBox="0 0 320 160"><path d="M312 0 V60 Q312 86 286 86 H36 Q10 86 10 112 V160" fill="none" stroke="var(--line)" stroke-width="2"/></svg>

<!-- WHY CHOOSE US -->
<div class="photo" style="left:435px;top:3578px;width:765px;height:526px;background:linear-gradient(90deg,rgba(255,255,255,1) 0%,rgba(214,220,228,.7) 22%,#c9cdd2 45%,#d8c7a8 65%,#bfc6cf 100%)" role="img" aria-label="Photo of three smiling colleagues working together at a laptop"></div>
<h2 class="h2" style="left:123px;top:3618px;color:var(--navy)"><span class="thin">WHY</span> CHOOSE US</h2>
<div class="underline" style="left:123px;top:3663px;width:60px"></div>
<p class="abs" style="left:125px;top:3690px;width:360px;font-size:14px;line-height:27px;font-weight:700;color:var(--ink)">Lorem Ipsum is simply dummy text of the printing and typesetting industry.</p>
<p class="para" style="left:125px;top:3768px;width:340px">We know, through our personal experiences gained as leaders, that the first 100 days in a critical transition are a crucible of leadership – when managed well, leaders build cohesive teams that succeed.</p>
<a class="btn" style="left:123px;top:3930px;width:153px;height:42px;font-size:12px">LEARN MORE</a>

<!-- CONTACT -->
<section class="contact-band">
  <svg class="abs" style="left:114px;top:80px" width="404" height="316" viewBox="0 0 404 316">
    <defs><linearGradient id="gBlob" x1="0" y1="0" x2="1" y2="1"><stop offset="0" stop-color="#1a6fd0"/><stop offset="1" stop-color="#0a3f8a"/></linearGradient></defs>
    <path d="M70 40 C150 -10 300 0 370 60 C420 110 400 230 360 280 C320 330 220 316 150 290 C80 264 10 230 2 160 C-4 110 20 70 70 40 Z" fill="url(#gBlob)"/>
  </svg>
  <h2 class="abs" style="left:157px;top:158px;color:var(--white);font-size:19px;font-weight:600;line-height:26px">LEAVE US A MESSAGE &amp;<br><b style="font-size:24px;font-weight:700">WE WILL CONTACT YOU</b></h2>
  <div class="abs" style="left:157px;top:222px;width:40px;height:2px;background:var(--white)"></div>
  <p class="abs" style="left:157px;top:238px;width:285px;color:#e4edfa;font-size:13.5px;line-height:22px">Lorem Ipsum is simply dummy text of the printing and typesetting industry. Lorem Ipsum has been</p>

  <div class="field" style="left:549px;top:129px;width:259px;height:40px"><svg width="14" height="14" viewBox="0 0 14 14" fill="none" stroke="#8a92a0" stroke-width="1.4"><circle cx="7" cy="4.5" r="3"/><path d="M1.5 13 Q7 6.5 12.5 13"/></svg>First Name</div>
  <div class="field" style="left:816px;top:129px;width:257px;height:40px"><svg width="14" height="14" viewBox="0 0 14 14" fill="none" stroke="#8a92a0" stroke-width="1.4"><circle cx="7" cy="4.5" r="3"/><path d="M1.5 13 Q7 6.5 12.5 13"/></svg>Last Name</div>
  <div class="field" style="left:549px;top:180px;width:259px;height:40px"><svg width="14" height="14" viewBox="0 0 14 14"><path d="M2 1.5 L5 1.5 L6 4.5 L4.5 5.8 Q6 8.5 8.2 9.5 L9.5 8 L12.5 9 L12.5 12 Q6 12.5 2 6 Z" fill="#8a92a0"/></svg>Phone Number</div>
  <div class="field" style="left:816px;top:180px;width:257px;height:40px"><svg width="14" height="12" viewBox="0 0 14 12" fill="none" stroke="#8a92a0" stroke-width="1.4"><rect x="1" y="1" width="12" height="10"/><path d="M1 1 L7 6 L13 1"/></svg>E-mail</div>
  <div class="field area" style="left:549px;top:231px;width:524px;height:76px"><svg width="14" height="12" viewBox="0 0 14 12" fill="none" stroke="#8a92a0" stroke-width="1.4"><path d="M1 2 Q1 1 2 1 H12 Q13 1 13 2 V8 Q13 9 12 9 H5 L2 11 V9 Q1 9 1 8 Z"/></svg>Leave Message</div>
  <a class="btn" style="left:547px;top:326px;width:184px;height:45px;background:var(--blue-light);font-size:13px">SEND MESSAGE</a>
</section>

<!-- FOOTER -->
<footer class="footer">
  <div class="brand" style="left:123px;top:94px">
    <span class="brand-mark" style="width:24px;height:24px"></span>
    <div class="brand-name">Bold Harbor</div>
  </div>
  <div class="small" style="left:123px;top:139px;font-size:10.5px;line-height:18px">Copyright 2021 Bold Harbor<br>Privacy Policy &nbsp;|&nbsp; Contact</div>
  <span class="social" style="left:126px;top:200px"></span>
  <span class="social" style="left:154px;top:200px"></span>
  <span class="social" style="left:182px;top:200px"></span>

  <h5 style="left:449px;top:64px">CONTACT US</h5>
  <svg class="abs" style="left:449px;top:96px" width="16" height="22" viewBox="0 0 16 22"><path d="M8 1 C4 1 1 4 1 8 C1 13 8 21 8 21 C8 21 15 13 15 8 C15 4 12 1 8 1 Z" fill="none" stroke="#fff" stroke-width="1.6"/><circle cx="8" cy="8" r="2.6" fill="#fff"/></svg>
  <div class="small" style="left:477px;top:94px;line-height:18px">18 Linden Row, Easton<br>MA 02011</div>
  <svg class="abs" style="left:449px;top:152px" width="16" height="16" viewBox="0 0 14 14"><path d="M2 1.5 L5 1.5 L6 4.5 L4.5 5.8 Q6 8.5 8.2 9.5 L9.5 8 L12.5 9 L12.5 12 Q6 12.5 2 6 Z" fill="#fff"/></svg>
  <div class="small" style="left:477px;top:150px">Tel: (1300) 555 0182</div>
  <svg class="abs" style="left:449px;top:188px" width="18" height="14" viewBox="0 0 14 12" fill="none" stroke="#fff" stroke-width="1.3"><rect x="1" y="1" width="12" height="10"/><path d="M1 1 L7 6 L13 1"/></svg>
  <div class="small" style="left:477px;top:185px">Email: info@boldharbor.com</div>

  <h5 style="left:723px;top:64px">COMPANY</h5>
  <div class="small" style="left:723px;top:92px">About Us<br>Ou Process<br>Services<br>Blog<br>Contact</div>

  <h5 style="left:871px;top:64px">JOIN NEWSLETTER</h5>
  <div class="abs" style="left:871px;top:94px;width:212px;height:30px;border-radius:16px;background:var(--white);font-size:9.5px;color:#5a6270;padding:9px 0 0 22px">E-mail address</div>
  <a class="btn" style="left:876px;top:136px;width:120px;height:29px;font-size:10px">SUBSCRIBE</a>
</footer>

</body>
</html>
```